Cafe menu design

Hi there,

We need a editable menu layout and design to match our new cafe call: " Harlow Bean Roasters", we love the ideas of A4 clip board and self print out menu in black and white. ( Example as attached)

We would like the menu can be break down into category easy for customer to flip around and read. ( example as attached)

Category including the following:

- All day breakfast and Sandwich and Toast
- Main (Lunch&Dinner) and Pizza
- Dessert snacks and nibbles
- Hot and Cold Drinks
- Catering menu

Please find our logo and our current menu as attached for your information and convenience.
Updates

Dear Designers, Thank you for your time and submission, Please find our drink menu and logo as attached. Kind Regards,

Target Market(s)

Young family, young Couple, office and corporate staff

Industry/Entity Type

Cafe

Font styles to use
Serif
Sans Serif

```html
<!DOCTYPE html>
<html lang="en">
<head>
<meta charset="utf-8">
<title>Harlow Bean Roasters — Desserts, Snacks &amp; Nibbles</title>
<link rel="stylesheet" href="https://fonts.googleapis.com/css2?family=Montserrat:ital,wght@0,400;0,700;1,400&family=Courier+Prime&display=swap">
<style>
  :root {
    --paper: #f3f3f1;
    --ink: #161616;
    --ink-soft: #2b2b2b;
    --badge: #141414;
    --badge-text: #f3f3f1;
  }
  * { margin: 0; padding: 0; box-sizing: border-box; }
  html, body { width: 1031px; height: 1200px; overflow: hidden; background: var(--paper); }
  .menu-page { position: relative; width: 1031px; height: 1200px; background: var(--paper); color: var(--ink); font-family: "Montserrat", Arial, sans-serif; }

  .brand-tab {
    position: absolute; left: 446px; top: 0; width: 139px; height: 170px;
    background: var(--badge);
    display: flex; align-items: center; justify-content: center; text-align: center;
    padding: 0 14px;
  }
  .brand-name {
    color: var(--badge-text); font-family: "Montserrat", Arial, sans-serif;
    font-weight: 700; font-size: 15px; line-height: 1.35; letter-spacing: 0.5px; text-transform: lowercase;
  }

  .menu-frame { position: absolute; left: 0; top: 0; }

  .price-rule {
    position: absolute; left: 745px; top: 338px; height: 344px; width: 0;
    border-left: 2px dotted var(--ink);
  }

  .menu-line { position: absolute; right: 300px; white-space: nowrap; text-align: right; }
  .item-name { font-weight: 700; font-size: 13.5px; letter-spacing: 0.2px; }
  .item-desc { font-style: italic; font-size: 11.5px; color: var(--ink-soft); letter-spacing: 0.4px; }
  .item-size { font-size: 11.5px; color: var(--ink-soft); letter-spacing: 0.4px; }

  .price { position: absolute; left: 758px; font-weight: 700; font-size: 13.5px; white-space: nowrap; }
  .price sup { font-size: 7px; vertical-align: 6px; margin-right: 1px; }

  .cabinet-note {
    position: absolute; left: 0; width: 1031px; top: 1045px; text-align: center;
    font-family: "Courier Prime", "Courier New", monospace; font-size: 15.5px; line-height: 21px;
    letter-spacing: 4.1px; text-transform: uppercase; color: var(--ink);
  }

  .section-rule { position: absolute; left: 22px; right: 22px; top: 1129px; border-top: 3px dotted var(--ink); }
  .section-title {
    position: absolute; left: 0; width: 1031px; top: 1144px; text-align: center;
    font-family: "Courier Prime", "Courier New", monospace; font-size: 21px;
    letter-spacing: 5.5px; text-transform: uppercase; color: var(--ink);
  }
</style>
</head>
<body>
<main class="menu-page">
  <header class="brand-tab">
    <span class="brand-name">harlow bean roasters</span>
  </header>

  <svg class="menu-frame" width="1031" height="1200" viewBox="0 0 1031 1200" aria-hidden="true">
    <path d="M94 193 H938 L950 205 V1098 L938 1110 H94 L82 1098 V205 Z" fill="none" stroke="#161616" stroke-width="1.5"/>
    <path d="M98 198 H934 L945 209 V1094 L934 1105 H98 L87 1094 V209 Z" fill="none" stroke="#161616" stroke-width="1.5"/>
  </svg>

  <div class="price-rule"></div>

  <div class="menu-line item-name" style="top:353px">bread &amp; butter pudding</div>
  <div class="menu-line item-desc" style="top:372px">served warm with fresh cream</div>
  <div class="price" style="top:353px"><sup>$</sup>7</div>

  <div class="menu-line item-name" style="top:396px">melting belgian chocolate pudding</div>
  <div class="menu-line item-desc" style="top:415px">served warm with ice cream</div>
  <div class="price" style="top:396px"><sup>$</sup>7</div>

  <div class="menu-line item-name" style="top:439px">american brownie</div>
  <div class="menu-line item-desc" style="top:458px">with fresh cream</div>
  <div class="price" style="top:439px"><sup>$</sup>7</div>

  <div class="menu-line item-name" style="top:482px">honey pancake</div>
  <div class="menu-line item-desc" style="top:501px">with golden maple syrup, fresh cut banana &amp; vanilla ice cream</div>
  <div class="price" style="top:482px"><sup>$</sup>15</div>

  <div class="menu-line item-name" style="top:525px">belgian chocolate waffles</div>
  <div class="menu-line item-desc" style="top:544px">crunchy waffles with belgian chocolate sauce</div>
  <div class="menu-line item-size" style="top:561px">good for 1 •</div>
  <div class="price" style="top:559px"><sup>$</sup>6</div>
  <div class="menu-line item-size" style="top:577px">good for 2 •</div>
  <div class="price" style="top:575px"><sup>$</sup>10</div>

  <div class="menu-line item-name" style="top:601px">belgian chocolate waffles &amp; ice cream</div>
  <div class="menu-line item-desc" style="top:620px">belgian waffles, fresh banana, vanilla ice cream chocolate sauce</div>
  <div class="menu-line item-size" style="top:637px">good for 1 •</div>
  <div class="price" style="top:635px"><sup>$</sup>8.50</div>
  <div class="menu-line item-size" style="top:653px">good for 2 •</div>
  <div class="price" style="top:651px"><sup>$</sup>15</div>

  <p class="cabinet-note">For more selection of cheesecakes, tarts &amp; desserts,<br>please check out our cake display cabinet.</p>

  <div class="section-rule"></div>
  <h1 class="section-title">Desserts, snacks &amp; nibbles</h1>
</main>
</body>
</html>
```